Banner Ad for Resume Services Website

The add is for this web site: www.BrightFolioDesk.com

The site offers 4 different services:

- Resume Writing (by a Certified Professional Resume Writer)
- Resume Posting (posts your resume to 85 job sites)
- Resume Distribution (sends your resume to hundreds of recruiters)
- Resume Online website (created an online resume with a domain name to your name)

Colors to be used are Blue, Yellow, etc... please check the website for inspiration.

Check the web site to learn more.

Target Market(s)

Unemployed, Professionals who want to switch jobs, etc..

Industry/Entity Type

Learn

Requirements
Must have
• We definitely one this to be included on the banner:

"Free Resume Samples"

in order to attract clicks.
Nice to have
• Some of the words we suggest to include on the banner are:

"How Good is Your Resume? Ask a Professional !"

Should not have
• No animation !

Do not place the LOGO on the banner as our LOGO might change in the near future. If you already submitted a banner with the LOGO on it, you can replace it with any other graphic that has a Resume/Jobs/BusinessStaff related theme.

```html
<!DOCTYPE html>
<html lang="en">
<head>
<meta charset="utf-8">
<title>Free Resume Samples – BrightFolioDesk</title>
<link href="https://fonts.googleapis.com/css2?family=Arimo:wght@400;700&display=swap" rel="stylesheet">
<style>
  :root {
    --blue-light: #2f74d6;
    --blue-mid: #1a57b8;
    --blue-deep: #0b3a8e;
    --white: #ffffff;
    --orange-top: #ff8a2a;
    --orange-bottom: #e85a05;
    --orange-edge: #c94a00;
    --photo-light: #c9ccd2;
    --photo-dark: #4a5262;
  }
  * { margin: 0; padding: 0; box-sizing: border-box; }
  html, body { width: 1200px; height: 148px; overflow: hidden; background: var(--white); }
  .banner {
    position: relative;
    width: 1200px;
    height: 148px;
    overflow: hidden;
    font-family: "Arimo", Arial, sans-serif;
    background:
      radial-gradient(ellipse 520px 200px at 560px 40px, var(--blue-light), transparent 70%),
      linear-gradient(90deg, var(--blue-mid) 0%, var(--blue-mid) 45%, var(--blue-deep) 100%);
  }
  .team-photo-frame {
    position: absolute;
    left: 0; top: 0;
    width: 360px; height: 148px;
  }
  .headline-group {
    position: absolute;
    left: 380px;
    width: 500px;
    top: 26px;
    text-align: center;
    color: var(--white);
  }
  .headline {
    font-weight: 700;
    font-size: 50px;
    line-height: 58px;
    letter-spacing: -0.3px;
    text-shadow: 0 2px 3px rgba(0,0,0,0.25);
  }
  .subline {
    font-weight: 400;
    font-size: 36px;
    line-height: 44px;
    margin-top: 2px;
  }
  .cta-button {
    position: absolute;
    left: 898px;
    top: 46px;
    width: 280px;
    height: 56px;
    border-radius: 8px;
    border: 2px solid var(--orange-edge);
    background: linear-gradient(180deg, var(--orange-top), var(--orange-bottom));
    box-shadow: 0 3px 6px rgba(0,0,0,0.3), inset 0 1px 0 rgba(255,255,255,0.4);
    color: var(--white);
    font-weight: 700;
    font-size: 26px;
    display: flex;
    align-items: center;
    justify-content: center;
    text-shadow: 0 1px 2px rgba(0,0,0,0.25);
  }
</style>
</head>
<body>
  <div class="banner">
    <svg class="team-photo-frame" viewBox="0 0 360 148" width="360" height="148">
      <defs>
        <linearGradient id="teamPhotoTone" x1="0" y1="0" x2="1" y2="1">
          <stop offset="0" stop-color="var(--photo-dark)"/>
          <stop offset="0.5" stop-color="var(--photo-light)"/>
          <stop offset="1" stop-color="var(--photo-dark)"/>
        </linearGradient>
      </defs>
      <polygon points="0,0 300,0 340,74 300,148 0,148" fill="url(#teamPhotoTone)"
               role="img" aria-label="Photo of three business professionals reviewing a resume at a desk"/>
      <polyline points="300,-4 340,74 300,152" fill="none" stroke="var(--white)" stroke-width="10"/>
    </svg>

    <div class="headline-group">
      <p class="headline">Free Resume Samples</p>
      <p class="subline">How Good is Your Resume?</p>
    </div>

    <div class="cta-button">Ask a Professional !</div>
  </div>
</body>
</html>
```